Business card for a new innovative and professional lawn care business

We need a business card design for a new lawn care business in Halifax NS Canada. We offer lawn services in Halifax & Bedford. Our services offered include lawn care, garden services, and property maintenance. We take pride in our work and are experienced at what we do. I would like to see a design that is double sided. On the backside I would like the something simple (maybe my logo preferably on blackround (linked below) with website link, Friendbook page or something). The front I want to include contact info:
Darren Maple
phone 902-555-0148
email - darrensyardworks.ca
facebook - Friendbook.com/darrensyardworks
Snapgram maybe ? - snapgram.com/darrenyardworks
Serving Halifax and Bedford for 5 years?
I don't want it to have too much information as I will be passing them out in aim to visit website, or call !
We do want it to include lawn care, garden services and property maintenance.
Basic, catchy, and modern looking !
Logo attached below !

Target Market(s)

Passing business cards to everyone I meet or interact with.

Industry/Entity Type

Lawn Care

Contact Information for Business Card

Double sided with some basic information, with catchy colours and easy to look at.

Font styles to use
Sans Serif

Requirements
Must have
• Must be double sided and have :
• Name, Phone, Email, FB, Website, and 3 main services offered - lawn care, property maintenance, garden services
Nice to have
• Would be nice to have instagram link if it goes well on there
Should not have
• Don't want too much writing or images that are distracting

```html
<!DOCTYPE html>
<html lang="en">
<head>
<meta charset="utf-8">
<title>Darren's Yard Works – Business Card</title>
<link href="https://fonts.googleapis.com/css2?family=Open+Sans:wght@400;600;700&display=swap" rel="stylesheet">
<style>
  :root{
    --page:#e9e9ea;
    --frame-grey:#454545;
    --panel:#2a2a2a;
    --orange:#e0761c;
    --green:#6cc140;
    --white:#ffffff;
    --soft:#d9d9d9;
    --photo-dark:#1f1f1f;
    --photo-mid:#5a5a5a;
  }
  *{box-sizing:border-box;margin:0;padding:0}
  html,body{width:1200px;height:800px;overflow:hidden}
  body{
    background:var(--page);
    font-family:"Open Sans",sans-serif;
    display:flex;align-items:center;justify-content:center;gap:40px;
  }
  .card{
    position:relative;width:540px;height:310px;
    background:var(--frame-grey);
    box-shadow:0 6px 18px rgba(0,0,0,.18);
    overflow:hidden;
  }
  .strip{position:absolute;background:var(--orange)}
  .panel{
    position:absolute;left:22px;top:22px;width:496px;height:266px;
    background:var(--panel);overflow:hidden;
  }

  /* front */
  .front .strip--left{left:0;top:0;width:22px;height:310px}
  .front .strip--top{left:0;top:0;width:230px;height:22px}
  .front .strip--bottom{left:0;bottom:0;width:330px;height:22px}
  .photo{
    position:absolute;left:0;top:0;width:180px;height:266px;
    clip-path:polygon(0 0,152px 0,180px 266px,0 266px);
    background:linear-gradient(160deg,var(--photo-dark) 0%,var(--photo-mid) 45%,#3a3a3a 100%);
  }
  .rule{position:absolute;left:0;top:0;pointer-events:none}
  .brand{
    position:absolute;left:18px;top:190px;
    display:flex;align-items:center;gap:7px;
    color:var(--green);font-weight:700;font-size:17px;line-height:1.05;
    text-transform:uppercase;letter-spacing:.5px;
  }
  .brand__dot{width:10px;height:10px;border-radius:50%;background:var(--green);flex:none}
  .contact-block{position:absolute;right:66px;top:42px;text-align:right}
  .name{font-weight:700;font-size:19px;color:var(--white);letter-spacing:.4px}
  .phone{font-size:15px;color:var(--soft);letter-spacing:.5px;margin-top:2px}
  .contact-block,.service{border-right:2px solid var(--orange);padding-right:3px}
  .services{position:absolute;right:66px;top:148px;text-align:right;display:flex;flex-direction:column;align-items:flex-end;gap:12px}
  .service{font-size:15px;color:var(--white);letter-spacing:.5px;line-height:1.1}

  /* back */
  .back .strip--right{right:0;top:0;width:22px;height:310px}
  .back .strip--top{right:0;top:0;width:52px;height:22px}
  .back .strip--bottom{right:0;bottom:0;width:322px;height:22px}
  .back .brand{position:absolute;left:30px;top:34px;font-size:22px}
  .links{position:absolute;left:30px;top:92px;list-style:none;display:flex;flex-direction:column;gap:9px}
  .links li{display:flex;align-items:center;gap:8px;color:var(--white);font-size:14px;letter-spacing:.3px}
  .links .dot{width:13px;height:13px;border-radius:50%;background:var(--orange);flex:none}
  .leaf-area{
    position:absolute;right:30px;bottom:16px;width:190px;height:90px;
    background:radial-gradient(ellipse at center,#323232 0%,var(--panel) 75%);
  }
</style>
</head>
<body>

<article class="card front" aria-label="Business card front">
  <div class="strip strip--left"></div>
  <div class="strip strip--top"></div>
  <div class="strip strip--bottom"></div>
  <div class="panel">
    <div class="photo" role="img" aria-label="Black and white photo of a lawn mower cutting grass"></div>
    <svg class="rule" width="496" height="266" viewBox="0 0 496 266" aria-hidden="true">
      <line x1="152" y1="0" x2="180" y2="266" stroke="#fff" stroke-width="2"/>
    </svg>
    <div class="brand"><span class="brand__dot"></span>Darren's<br>Yard Works</div>
    <div class="contact-block">
      <p class="name">Darren Maple</p>
      <p class="phone">902-555-0148</p>
    </div>
    <div class="services">
      <p class="service">Lawn Care</p>
      <p class="service">Property Maintenance</p>
      <p class="service">Garden Services</p>
    </div>
  </div>
</article>

<article class="card back" aria-label="Business card back">
  <div class="strip strip--right"></div>
  <div class="strip strip--top"></div>
  <div class="strip strip--bottom"></div>
  <div class="panel">
    <div class="leaf-area" role="img" aria-label="Faint outline of two leaves"></div>
    <div class="brand"><span class="brand__dot"></span>Darren's Yard Works</div>
    <ul class="links">
      <li><span class="dot"></span>darrensyardworks.ca</li>
      <li><span class="dot"></span>Friendbook.com/darrensyardworks</li>
      <li><span class="dot"></span>snapgram.com/darrenyardworks</li>
    </ul>
    <svg class="rule" width="496" height="266" viewBox="0 0 496 266" aria-hidden="true">
      <line x1="170" y1="240" x2="470" y2="100" stroke="#fff" stroke-width="1.5"/>
    </svg>
  </div>
</article>

</body>
</html>
```